Business Postcard Design for Personal Training Company

Need a postcard design for my company called "Maple Stride" Colors are Navy Blue, Blue, Grey and White.

On the front I want there to be pictures and it to feature a box that says "Free Consultation + 50% off your first session!"

And somehow to feature the following phrases " Lose Weight. Gain Muscle."
"Customized Personal training using Q-Pulse, the latest technology in fitness. Reach your fitness goals in just two 25-min sessions per week"

Also want featured the following phrases (maybe on back):

"up to 18 times more effective than a conventional gym workout"

I need the back of the postcard to have all my business information:

Address: 372 Dovercrest Ave, Building B Suite 218, Costa Mesa CA 92631
Website: maple-stride.example
Phone #: (949) 555-0137
E-mail: maplestridehealth@mailbox.example

I am going to upload my logo, before and after pictures and pictures of people training on the device. Feel free to use as many/or little photos as you want.

Target Market(s)

Wealthy Adults 40+ years old looking for a personal trainer

Industry/Entity Type

Personal Trainer

Colors
0455a3
85cae6
aaaaaa
ffffff

Requirements
Must have
• At least two of the before and after photos, and two or more photos of people working out on the device.

```html
<!DOCTYPE html>
<html lang="en">
<head>
<meta charset="utf-8">
<title>Maple Stride Postcard</title>
<link href="https://fonts.googleapis.com/css2?family=Open+Sans:wght@400;600;700&display=swap" rel="stylesheet">
<style>
  :root {
    --navy: #0455a3;
    --navy-deep: #063a78;
    --sky: #85cae6;
    --grey: #aaaaaa;
    --paper: #ffffff;
    --ink: #333a40;
    --stage: #ececec;
  }
  * { box-sizing: border-box; margin: 0; padding: 0; }
  html, body { width: 831px; height: 1200px; overflow: hidden; background: var(--stage); font-family: "Open Sans", Arial, sans-serif; }
  .card { position: absolute; left: 112px; width: 631px; height: 489px; background: var(--paper); overflow: hidden; box-shadow: 0 4px 12px rgba(0,0,0,.25); }
  .card--front { top: 85px; }
  .card--back { top: 632px; }
  .photo { position: absolute; }
  .shapes { position: absolute; left: 0; top: 0; }

  .front-photo { left: 0; top: 0; width: 320px; height: 384px; background: linear-gradient(160deg, #d7dde2 0%, #8a9aa8 45%, #2f4f8f 75%, #3a3f4a 100%); }
  .brand { position: absolute; left: 392px; top: 30px; display: flex; align-items: center; gap: 8px; }
  .brand__mark { width: 22px; height: 22px; border-radius: 50%; background: var(--sky); }
  .brand__name { font-weight: 700; font-size: 17px; color: var(--navy); letter-spacing: .5px; }
  .tagline { position: absolute; left: 300px; width: 310px; top: 104px; text-align: center; color: var(--navy); font-weight: 700; font-size: 18px; }
  .offer { position: absolute; left: 262px; width: 369px; top: 142px; text-align: center; color: var(--paper); font-weight: 700; line-height: 1.3; }
  .offer__line1 { font-size: 21px; letter-spacing: .5px; }
  .offer__line2 { font-size: 22px; }
  .pitch { position: absolute; left: 312px; width: 290px; top: 234px; text-align: center; color: var(--ink); font-size: 15px; line-height: 25px; }
  .snapshot { position: absolute; left: 468px; top: 336px; width: 142px; height: 86px; background: var(--paper); padding: 4px; transform: rotate(-4deg); box-shadow: 0 2px 6px rgba(0,0,0,.35); display: flex; gap: 4px; }
  .snapshot .photo { position: relative; flex: 1; height: 100%; }
  .snapshot__before { background: linear-gradient(180deg, #6b7b8a, #2c3440); }
  .snapshot__after { background: linear-gradient(180deg, #7c8a96, #262c34); }
  .snapshot__label { position: absolute; bottom: 2px; left: 4px; font-size: 7px; color: var(--paper); font-weight: 600; }

  .address { position: absolute; left: 10px; color: var(--paper); font-size: 11px; line-height: 17px; white-space: nowrap; }
  .card--front .address { top: 410px; }
  .card--back .address { top: 412px; }
  .cta { position: absolute; color: var(--navy); white-space: nowrap; }
  .cta strong { font-weight: 700; }
  .card--front .cta { left: 262px; top: 398px; font-size: 14px; line-height: 25px; }
  .card--front .cta .phone { font-size: 16px; font-weight: 700; }
  .card--back .cta { left: 250px; width: 381px; top: 394px; text-align: center; font-size: 16px; line-height: 28px; }
  .card--back .cta .phone { font-size: 18px; font-weight: 700; }

  .back-photo { left: 0; top: 0; width: 357px; height: 376px; background: linear-gradient(180deg, #c9cfd4 0%, #9aa7b1 30%, #2a2f38 55%, #6f7f6a 85%, #8d8d80 100%); }
  .claim { position: absolute; left: 0; top: 166px; width: 372px; text-align: center; color: var(--paper); font-weight: 700; font-size: 14px; line-height: 21px; padding-top: 5px; }
  .bubble { width: 124px; height: 124px; border-radius: 50%; border: 4px solid var(--sky); top: 17px; }
  .bubble--one { left: 356px; background: linear-gradient(180deg, #a9c3d6, #7c8f76); }
  .bubble--two { left: 491px; background: linear-gradient(180deg, #c8ccd0, #3c4250); }
  .progress { top: 152px; width: 134px; height: 224px; }
  .progress--before { left: 358px; background: linear-gradient(180deg, #e4e4e0, #bfb8ae 50%, #2c2c30 90%); }
  .progress--after { left: 496px; background: linear-gradient(180deg, #e6e6e4, #bdb4a8 50%, #2a2a2e 90%); }
  .progress__label { position: absolute; left: 12px; bottom: 6px; color: var(--paper); font-size: 9px; font-weight: 600; }
</style>
</head>
<body>

<section class="card card--front" aria-label="Postcard front">
  <div class="photo front-photo" role="img" aria-label="Trainer guiding a client in a muscle-stimulation suit on an exercise ball"></div>
  <svg class="shapes" width="631" height="489" viewBox="0 0 631 489" aria-hidden="true">
    <defs>
      <linearGradient id="panelTone" x1="0" y1="0" x2="0" y2="1">
        <stop offset="0" stop-color="#f1f1f1"/>
        <stop offset=".35" stop-color="#ffffff"/>
      </linearGradient>
    </defs>
    <path d="M300 0 C270 60 266 170 288 384 L631 384 L631 0 Z" fill="url(#panelTone)"/>
    <polygon points="256,133 631,133 631,222 239,222" fill="var(--navy)"/>
    <polygon points="256,133 300,133 283,222 239,222" fill="var(--navy-deep)"/>
    <rect x="0" y="384" width="631" height="105" fill="var(--paper)"/>
    <polygon points="228,384 631,384 631,468 254,468" fill="var(--sky)"/>
    <polygon points="0,395 232,395 252,489 0,489" fill="var(--navy)"/>
  </svg>

  <div class="brand"><span class="brand__mark"></span><span class="brand__name">MAPLE STRIDE</span></div>
  <h2 class="tagline">LOSE WEIGHT. GAIN MUSCLE.</h2>
  <div class="offer">
    <p class="offer__line1">FREE CONSULTATION</p>
    <p class="offer__line2">+ 50% off your first session!</p>
  </div>
  <p class="pitch">Customized Personal training using<br>Q-Pulse, the latest technology in fitness.<br>Reach your fitness goals in just two<br>25-min sessions per week</p>
  <div class="snapshot">
    <div class="photo snapshot__before" role="img" aria-label="Client before training"><span class="snapshot__label">Session 1</span></div>
    <div class="photo snapshot__after" role="img" aria-label="Client after training"><span class="snapshot__label">Session 30</span></div>
  </div>
  <p class="address">372 Dovercrest Ave,<br>Building B Suite 218,<br>Costa Mesa CA 92631<br>maplestridehealth@mailbox.example</p>
  <p class="cta">Call <span class="phone">(949) 555-0137</span> today<br>Or visit <strong>maple-stride.example</strong> for information.</p>
</section>

<section class="card card--back" aria-label="Postcard back">
  <div class="photo back-photo" role="img" aria-label="Woman in a training suit lifting dumbbells on a terrace overlooking a harbor"></div>
  <svg class="shapes" width="631" height="489" viewBox="0 0 631 489" aria-hidden="true">
    <path d="M286 0 C330 4 356 40 357 96 L357 0 Z" fill="var(--paper)"/>
    <rect x="0" y="376" width="631" height="113" fill="#e6e6e6"/>
    <polygon points="0,166 372,166 386,217 0,217" fill="var(--navy)"/>
    <polygon points="214,384 631,384 631,469 240,469" fill="var(--sky)"/>
    <polygon points="0,397 232,397 252,489 0,489" fill="var(--navy)"/>
  </svg>
  <p class="claim">UP TO 18 TIMES MORE EFFECTIVE<br>THAN A CONVENTIONAL GYM WORKOUT</p>
  <div class="photo bubble bubble--one" role="img" aria-label="Trainer and client exercising outdoors"></div>
  <div class="photo bubble bubble--two" role="img" aria-label="Trainer and client exercising indoors"></div>
  <div class="photo progress progress--before" role="img" aria-label="Client flexing arms before training"><span class="progress__label">Session 1</span></div>
  <div class="photo progress progress--after" role="img" aria-label="Client flexing arms after training"><span class="progress__label">Session 30</span></div>
  <p class="address">372 Dovercrest Ave,<br>Building B Suite 218,<br>Costa Mesa CA 92631<br>maplestridehealth@mailbox.example</p>
  <p class="cta">Call <span class="phone">(949) 555-0137</span> today<br>Or visit <strong>maple-stride.example</strong> for information.</p>
</section>

</body>
</html>
```